bottle label/ product label for smoothies (ultra fresh)

Please create a bottle label for our smoothies for retail distribution.
It's important that the following key features are clearly stated:

Ultra-fresh

Handmade

No preservatives

Not heat-treated

No added sugar

The base of the product label should be transparent, so that the color and content of the smoothie can be seen clearly.

We are a young, dynamic company. Our values are honesty, ultra-freshness, and authenticity — and we are the only ones producing this type of product in our country. We are positioned in the premium segment.

Design style: Modern, clean, and natural — but not playful or childish.

Example product: Kelu Kelu (Mango, Pineapple, Lemon, Passion Fruit, Orange)

Wenn du möchtest, kann ich auch gleich einen konkreten Vorschlag für das Etikettendesign auf Englisch oder einen Entwurfstext für das Label selbst erstellen. Sag einfach Bescheid!

Target Market(s)

trade - convenience

Industry/Entity Type

trade

Font styles to use
Sans Serif

Requirements
Must have
• sales- features: Ultra-fresh Handmade No preservatives Not heat-treated No added sugar

```html
<!DOCTYPE html>
<html lang="en">
<head>
<meta charset="UTF-8">
<title>Solvara Mango Smoothie – Bottle Label</title>
<link rel="stylesheet" href="https://fonts.googleapis.com/css2?family=Poppins:wght@600&family=Saira:ital,wght@1,800&family=Montserrat:wght@600;800&family=Oswald:wght@700&display=swap">
<style>
  :root {
    --canvas: #eeeeee;
    --label-clear: #f7f7f5;
    --yellow: #ffd100;
    --green: #0b5223;
    --ink: #111111;
    --red: #e32626;
    --mango-light: #ffe066;
    --mango-mid: #f7b52b;
    --mango-deep: #e8841c;
  }
  * { box-sizing: border-box; margin: 0; padding: 0; }
  html, body { width: 1200px; height: 1200px; overflow: hidden; }
  body { background: var(--canvas); position: relative; font-family: "Montserrat", sans-serif; }

  .label {
    position: absolute; left: 320px; top: 80px;
    width: 560px; height: 1040px;
    background: var(--label-clear);
    overflow: hidden;
  }
  .label-header { position: absolute; left: 0; top: 0; width: 560px; height: 240px; }
  .brand-name {
    position: absolute; left: 0; top: 55px; width: 560px;
    text-align: center;
    font-family: "Poppins", sans-serif; font-weight: 600;
    font-size: 104px; line-height: 1; color: var(--ink); letter-spacing: -2px;
  }
  .fruit-icon {
    position: absolute; left: 470px; top: 232px; width: 62px; height: 70px;
    border-radius: 50%;
    background: radial-gradient(circle at 35% 35%, var(--mango-light), var(--mango-mid) 60%, var(--mango-deep));
  }
  .flavour {
    position: absolute; left: 0; top: 262px; width: 560px; text-align: center;
    font-family: "Saira", sans-serif; font-style: italic; font-weight: 800;
    color: var(--green); line-height: 1;
  }
  .flavour-name { display: block; font-size: 112px; letter-spacing: 2px; }
  .flavour-type {
    display: block; font-size: 48px; margin-top: -6px; padding-left: 130px;
    -webkit-text-stroke: 2px var(--yellow); paint-order: stroke fill;
  }
  .claim-pill {
    position: absolute; left: 82px; top: 428px; width: 400px; height: 64px;
    background: var(--yellow); border-radius: 32px;
    display: flex; align-items: center; justify-content: center;
    font-weight: 800; font-size: 38px; color: var(--ink);
  }
  .claim-sugar {
    position: absolute; left: 0; top: 504px; width: 560px; text-align: center;
    font-weight: 600; font-size: 22px; color: var(--red);
  }
  .claim-band {
    position: absolute; left: 0; top: 548px; width: 560px; height: 80px;
    background: var(--yellow);
    display: flex; align-items: center; justify-content: center;
    font-family: "Oswald", sans-serif; font-weight: 700; font-size: 30px;
    color: var(--green); letter-spacing: -0.5px;
  }
  .fruit-visual {
    position: absolute; left: 0; top: 640px; width: 560px; height: 360px;
    background: radial-gradient(ellipse at 50% 60%, var(--mango-light) 0%, var(--mango-mid) 45%, var(--mango-deep) 75%, var(--label-clear) 100%);
  }
  .volume-badge {
    position: absolute; left: 12px; top: 648px; width: 150px; height: 150px;
    border-radius: 50%; background: var(--green);
    display: flex; align-items: center; justify-content: center;
    font-family: "Oswald", sans-serif; font-weight: 700; font-size: 38px; color: #fff;
  }
  .handmade-pill {
    position: absolute; left: 180px; top: 648px; width: 365px; height: 70px;
    background: var(--green); border-radius: 35px;
    display: flex; align-items: center; gap: 14px; padding-left: 14px;
    font-weight: 800; font-style: italic; font-size: 36px; color: #fff;
  }
  .handmade-seal { width: 48px; height: 48px; border-radius: 50%; background: #fff; flex: none; }
  .label-footer { position: absolute; left: 0; bottom: 0; width: 560px; height: 40px; background: var(--green); }
</style>
</head>
<body>
  <main class="label">
    <svg class="label-header" viewBox="0 0 560 240" aria-hidden="true">
      <path d="M0 0 H560 V185 C480 235 80 235 0 140 Z" fill="var(--green)"/>
      <path d="M0 0 H560 V150 C470 215 90 215 0 110 Z" fill="var(--yellow)"/>
    </svg>
    <div class="brand-name">Solvara</div>

    <div class="fruit-icon" role="img" aria-label="Small mango with leaf"></div>

    <h1 class="flavour">
      <span class="flavour-name">MANGO</span>
      <span class="flavour-type">SMOOTHIE</span>
    </h1>

    <div class="claim-pill">ULTRA FRESH</div>
    <p class="claim-sugar">NO ADDED SUGAR</p>
    <div class="claim-band">NO PRESERVATIVES | NOT HEAT-TREATED</div>

    <div class="fruit-visual" role="img" aria-label="Whole mango and sliced mango with a juice splash"></div>

    <div class="volume-badge">750 ml</div>
    <div class="handmade-pill"><span class="handmade-seal"></span>HANDMADE</div>

    <div class="label-footer"></div>
  </main>
</body>
</html>
```